A book about police officer shootings needs a dynamic cover design

I've almost completed a book on officer involved shootings...a very hot topic today. The title is "R.K.T. Beyond The Silence Fell." (emphasis on "beyond the silence") It details three separate shooting incidents, all within the same law enforcement family.I need a professional looking book cover that helps capture the drama. I attached a file of something I put together that is close, but I am concerned about "readability" and want a more professional look. I included a photo that I took off the internet of a gun being shot. That particular photo can stay or go, or be altered, but I like the perspective of the photo being fired from the person behind it. I wanted the cover to have the characteristics and color of a police uniform, utilizing blues, silvers, and maybe a little gold. I'm concerned about making sure the font and colors are also easy to read. I also will be working on a website design for "Beyond The Silence.Com" once the book hits the market. The back cover will incorporate the same colors, but only be a picture and excerpts from the book. I've included both for your review.

Target Market(s)

Law Enforcement, Christian, Media

Font styles to use
Sans Serif

Requirements
Must have
• A professional and readable appearance, that captures the drama of the topic. All the wording on the sample cover I attached, unless you come up with something better. A gun being fired from the perspective of the officer pulling the trigger. The size of the book will be the standard 6 x 9 in size. "Beyond The Silence" will eventually be my website domain and social media promotion hashtag.
Nice to have
• I would like the cover to incorporate the colors of a police uniform and badge, traditionally, navy blue, silver and some gold.
Should not have
• No police badge with a black band across. Not my topic.

```html
<!DOCTYPE html>
<html lang="en">
<head>
<meta charset="utf-8">
<title>R.K.T. Beyond The Silence Fell. — Book Cover</title>
<link href="https://fonts.googleapis.com/css2?family=Anton&family=Oswald:wght@500;700&display=swap" rel="stylesheet">
<style>
  :root {
    --page: #ececec;
    --paper: #ffffff;
    --ink: #111111;
    --alert-red: #e0141b;
    --badge-gold: #f7e21a;
    --navy: #0b1a3d;
    --navy-deep: #050b1f;
    --smoke: #eef3f8;
    --silver: #dfe3ea;
    --wood: #7a3a22;
    --brass: #c9a24a;
  }
  * { margin: 0; padding: 0; box-sizing: border-box; }
  html, body {
    width: 1082px; height: 1200px; overflow: hidden;
    background: var(--page);
  }
  .canvas {
    width: 1082px; height: 1200px;
    display: flex; align-items: center; justify-content: center;
  }
  .cover {
    position: relative;
    width: 747px; height: 1120px;
    background: var(--paper);
    overflow: hidden;
    box-shadow: 0 6px 24px rgba(0,0,0,0.25);
  }
  .tagline {
    position: absolute; top: 0; left: 0; right: 0; height: 92px;
    display: flex; align-items: center; justify-content: center;
    font-family: "Oswald", sans-serif; font-weight: 700;
    font-size: 30px; letter-spacing: 0.5px; color: var(--ink);
    text-transform: uppercase;
    background: var(--paper);
    z-index: 2;
  }
  .hero-art {
    position: absolute; top: 80px; left: 0; right: 0; bottom: 160px;
    background:
      radial-gradient(ellipse 60% 30% at 55% 12%, var(--smoke) 0%, rgba(238,243,248,0.9) 40%, rgba(238,243,248,0) 75%),
      radial-gradient(ellipse 35% 12% at 45% 34%, #5a4030 0%, rgba(60,40,30,0.6) 50%, rgba(0,0,0,0) 100%),
      radial-gradient(ellipse 50% 25% at 40% 70%, #3a6cf0 0%, rgba(31,79,216,0.6) 45%, rgba(5,11,31,0) 80%),
      linear-gradient(180deg, #f4f7fb 0%, #c9d6e6 20%, #2a3550 38%, #0e1a3a 52%, #1b3e9e 68%, #0a1430 100%);
  }
  .title-block {
    position: absolute; left: 200px; right: 22px; top: 470px;
    font-family: "Anton", sans-serif; font-weight: 400;
    text-transform: uppercase;
    z-index: 3;
  }
  .title-line { display: block; }
  .title-initials {
    font-size: 54px; line-height: 58px; color: var(--ink);
    text-shadow: 0 0 6px rgba(255,255,255,0.6);
  }
  .title-lead {
    font-size: 82px; line-height: 84px; color: var(--alert-red);
    -webkit-text-stroke: 2px var(--ink);
  }
  .title-main {
    font-size: 156px; line-height: 160px; color: var(--alert-red);
    -webkit-text-stroke: 3px var(--ink);
    letter-spacing: -1px;
  }
  .title-end {
    font-size: 86px; line-height: 92px; color: var(--badge-gold);
    -webkit-text-stroke: 2px var(--ink);
    text-align: right;
  }
  .story-band {
    position: absolute; left: 0; right: 0; top: 880px; height: 80px;
    padding-left: 160px;
    background: var(--badge-gold);
    display: flex; flex-direction: column; align-items: center; justify-content: center;
    font-family: "Oswald", sans-serif; font-weight: 500;
    font-size: 30px; line-height: 1.05; color: var(--ink);
    text-transform: uppercase;
    z-index: 3;
  }
  .story-line { display: block; }
  .story-emphasis { color: var(--alert-red); }
  .author-band {
    position: absolute; left: 0; right: 0; bottom: 0; height: 160px;
    background: linear-gradient(180deg, var(--navy) 0%, var(--navy-deep) 100%);
    display: flex; align-items: center; justify-content: center;
    padding-left: 160px;
    z-index: 2;
  }
  .author-name {
    font-family: "Oswald", sans-serif; font-weight: 700;
    font-size: 38px; letter-spacing: 1px; color: var(--silver);
    text-transform: uppercase;
  }
  .gavel-art {
    position: absolute; left: 18px; top: 850px; width: 170px; height: 190px;
    border-radius: 8px;
    background: radial-gradient(ellipse 60% 45% at 50% 45%, var(--brass) 0%, var(--wood) 55%, rgba(122,58,34,0) 100%);
    z-index: 4;
  }
</style>
</head>
<body>
  <main class="canvas">
    <section class="cover">
      <p class="tagline">It will happen, and it will come out of nowhere...</p>
      <div class="hero-art" role="img" aria-label="Photograph from behind an officer's hand firing a handgun, smoke bursting upward, blue police lights glowing below"></div>
      <h1 class="title-block">
        <span class="title-line title-initials">R.K.T.</span>
        <span class="title-line title-lead">Beyond The</span>
        <span class="title-line title-main">Silence</span>
        <span class="title-line title-end">Fell.</span>
      </h1>
      <div class="story-band">
        <span class="story-line">One <span class="story-emphasis">Law</span> Enforcement Family...</span>
        <span class="story-line">Three Life-Changing Stories</span>
      </div>
      <footer class="author-band">
        <span class="author-name">Lt. Dale Merrin</span>
      </footer>
      <div class="gavel-art" role="img" aria-label="Illustration of a wooden judge's gavel with brass bands resting on its block"></div>
    </section>
  </main>
</body>
</html>
```